Stationary package for VORELO
VORELO is an outdoor and camping supplies distribution company
Professional
Yousef K Haddadin
Director
#17 Sahra Trade Gardens
Dubai
UAE
pinetrail@mailbox-ex.test
www.vorelo-supply.test

```html
<!DOCTYPE html>
<html lang="en">
<head>
<meta charset="utf-8">
<title>VORELO — Business Card</title>
<link href="https://fonts.googleapis.com/css2?family=Arimo:wght@400;700&display=swap" rel="stylesheet">
<style>
  :root {
    --backdrop: #e4e4e4;
    --card: #ffffff;
    --ink: #3b3b3b;
    --ink-soft: #6a6a6a;
    --accent: #8a5a2b;
    --rule: #9a9a9a;
  }
  * { box-sizing: border-box; margin: 0; padding: 0; }
  html, body {
    width: 1200px; height: 758px; overflow: hidden;
    background: var(--backdrop);
    font-family: "Arimo", Arial, sans-serif;
    color: var(--ink);
  }
  .stage {
    width: 1200px; height: 758px;
    display: flex; align-items: center; justify-content: center; gap: 50px;
  }
  .card {
    position: relative;
    width: 540px; height: 310px;
    background: var(--card);
    box-shadow: 0 4px 14px rgba(0,0,0,0.18);
  }
  .wordmark {
    font-weight: 700;
    color: var(--ink);
    letter-spacing: 1px;
    line-height: 1;
  }
  /* Front */
  .card--front .wordmark {
    position: absolute; left: 150px; top: 62px;
    font-size: 64px;
  }
  .contact {
    position: absolute; left: 40px; top: 170px;
    display: flex; align-items: stretch;
  }
  .identity { text-align: right; padding-right: 16px; width: 220px; }
  .identity .name { font-weight: 700; font-size: 17px; color: var(--ink); }
  .identity .role { font-size: 13px; color: var(--accent); margin-top: 3px; }
  .identity .address { font-size: 11px; color: var(--ink-soft); margin-top: 10px; line-height: 1.45; }
  .divider { width: 1px; background: var(--rule); }
  .details { padding-left: 14px; font-size: 11px; color: var(--ink-soft); }
  .details li { list-style: none; display: flex; align-items: center; gap: 7px; line-height: 1.6; }
  .details svg { width: 10px; height: 10px; fill: var(--ink); flex: none; }
  .details .web { font-weight: 700; font-size: 12px; color: var(--ink); margin-top: 12px; }
  /* Back */
  .card--back {
    display: flex; flex-direction: column; align-items: center; justify-content: center;
  }
  .card--back .wordmark { font-size: 78px; margin-top: -10px; }
  .card--back .web { font-weight: 700; font-size: 17px; color: var(--ink); margin-top: 38px; }
</style>
</head>
<body>
<main class="stage">
  <section class="card card--front">
    <div class="wordmark">VORELO</div>
    <div class="contact">
      <div class="identity">
        <p class="name">Yousef K Haddadin</p>
        <p class="role">Director</p>
        <p class="address">#17 Sahra Trade Gardens<br>Dubai, UAE</p>
      </div>
      <div class="divider"></div>
      <ul class="details">
        <li>
          <svg viewBox="0 0 10 10" aria-hidden="true"><path d="M2 0.5h2l0.8 2.2-1.2 0.9c0.5 1.2 1.3 2 2.5 2.5l0.9-1.2 2.2 0.8v2c0 0.6-0.5 1-1 1C4 8.7 1.3 6 1 1.5c0-0.5 0.4-1 1-1z"/></svg>
          +966500123456
        </li>
        <li>
          <svg viewBox="0 0 10 10" aria-hidden="true"><path d="M2 0.5h2l0.8 2.2-1.2 0.9c0.5 1.2 1.3 2 2.5 2.5l0.9-1.2 2.2 0.8v2c0 0.6-0.5 1-1 1C4 8.7 1.3 6 1 1.5c0-0.5 0.4-1 1-1z"/></svg>
          +966500654321
        </li>
        <li>
          <svg viewBox="0 0 10 10" aria-hidden="true"><path d="M0.5 2h9v6h-9z M0.5 2l4.5 3.5 4.5-3.5" fill="none" stroke="#3b3b3b" stroke-width="1"/></svg>
          pinetrail@mailbox-ex.test
        </li>
        <li class="web">www.vorelo-supply.test</li>
      </ul>
    </div>
  </section>

  <section class="card card--back">
    <div class="wordmark">VORELO</div>
    <p class="web">www.vorelo-supply.test</p>
  </section>
</main>
</body>
</html>
```